Business Card Design for Engineering Firm

Need a business card design for small mechanical and plumbing engineering form based in Utah. Design should be customizable for all employees.

```html
<!DOCTYPE html>
<html lang="en">
<head>
<meta charset="utf-8">
<title>Marlowe Engineering – Business Cards</title>
<link rel="stylesheet" href="https://fonts.googleapis.com/css2?family=Montserrat:wght@400;500;700&display=swap">
<style>
  :root {
    --brand-red: #8a161b;
    --ink: #1c1c1c;
    --slate: #4d4d4d;
    --paper: #ffffff;
    --backdrop: #2b2b2b;
  }
  * { margin: 0; padding: 0; box-sizing: border-box; }
  html, body { width: 1200px; height: 880px; overflow: hidden; }
  body {
    background: var(--backdrop);
    font-family: "Montserrat", Arial, sans-serif;
    position: relative;
  }
  .card {
    position: absolute;
    width: 560px;
    height: 320px;
    overflow: hidden;
    box-shadow: 0 10px 28px rgba(0,0,0,.45);
  }
  /* Front */
  .card-front {
    left: 70px; top: 80px;
    background: var(--brand-red);
    display: flex; align-items: center; justify-content: center;
  }
  .front-brand {
    display: flex; flex-direction: column; align-items: center; gap: 10px;
    color: #e9e9e9; font-weight: 700; text-align: center;
  }
  .front-brand .mark {
    width: 22px; height: 22px; background: #e9e9e9; margin-bottom: 8px;
  }
  .front-brand .name-main { font-size: 42px; letter-spacing: 1px; line-height: 1; }
  .front-brand .name-sub { font-size: 18px; letter-spacing: 9px; line-height: 1; }

  /* Back */
  .card-back {
    left: 570px; top: 480px;
    background: var(--paper);
  }
  .back-bands { position: absolute; left: 0; bottom: 0; width: 560px; height: 70px; }
  .back-brand {
    position: absolute; left: 40px; top: 110px; width: 230px;
    display: flex; flex-direction: column; align-items: center; gap: 8px;
    color: var(--brand-red); font-weight: 700; text-align: center;
  }
  .back-brand .mark { width: 18px; height: 18px; background: var(--brand-red); margin-bottom: 6px; }
  .back-brand .name-main { font-size: 30px; letter-spacing: .5px; line-height: 1; }
  .back-brand .name-sub { font-size: 13px; letter-spacing: 7px; line-height: 1; }
  .divider {
    position: absolute; left: 300px; top: 48px; width: 2px; height: 140px;
    background: var(--brand-red);
  }
  .contact { position: absolute; left: 322px; top: 44px; color: var(--ink); }
  .person-name { font-size: 20px; font-weight: 700; color: var(--slate); line-height: 1.1; }
  .person-name .surname { color: var(--brand-red); }
  .person-role { font-size: 12px; margin-top: 3px; }
  .address { font-size: 12px; margin-top: 12px; line-height: 1.35; }
  .contact-list { list-style: none; margin-top: 10px; font-size: 12px; }
  .contact-list li { display: flex; align-items: center; gap: 8px; line-height: 1.7; }
  .contact-list svg { width: 12px; height: 12px; fill: var(--brand-red); flex: none; }
</style>
</head>
<body>

<section class="card card-front" aria-label="Card front">
  <div class="front-brand">
    <span class="mark"></span>
    <span class="name-main">MARLOWE</span>
    <span class="name-sub">ENGINEERING</span>
  </div>
</section>

<section class="card card-back" aria-label="Card back">
  <div class="back-brand">
    <span class="mark"></span>
    <span class="name-main">MARLOWE</span>
    <span class="name-sub">ENGINEERING</span>
  </div>

  <div class="divider"></div>

  <div class="contact">
    <p class="person-name">DANIEL <span class="surname">MERCER</span></p>
    <p class="person-role">Co-Founder</p>
    <p class="address">P.O. BOX 44-12 STE-6<br>Alder Ave 17, Lindon</p>
    <ul class="contact-list">
      <li><svg viewBox="0 0 24 24"><path d="M6.6 10.8a15 15 0 0 0 6.6 6.6l2.2-2.2c.3-.3.7-.4 1-.2 1.1.4 2.3.6 3.6.6.6 0 1 .4 1 1V20c0 .6-.4 1-1 1A17 17 0 0 1 3 4c0-.6.4-1 1-1h3.5c.6 0 1 .4 1 1 0 1.3.2 2.5.6 3.6.1.3 0 .7-.2 1z"/></svg>801-555-0142</li>
      <li><svg viewBox="0 0 24 24"><path d="M2 5h20v14H2zm2 2v.5l8 5 8-5V7z"/></svg>hello@marlowe-mail.com</li>
      <li><svg viewBox="0 0 24 24"><circle cx="12" cy="12" r="10"/></svg>www.marlowe-web.com</li>
    </ul>
  </div>

  <svg class="back-bands" viewBox="0 0 560 70" preserveAspectRatio="none" aria-hidden="true">
    <polygon points="0,70 0,58 240,58 270,0 560,0 560,70" fill="#4d4d4d"/>
    <polygon points="270,70 300,12 560,12 560,70" fill="#8a161b"/>
  </svg>
</section>

</body>
</html>
```